Business Card Design for company

We want new business cards. We'd like something different-- yet still highly professional. Our tagline is Providing leadership, delivering success. Stock photos are ok, as long as they are relevant and look upscale.

Target Market(s)

Architecture/Business Management Consulting/Engineering Consulting

Contact Information for Business Card

dark gray background with pops of blue might be good, but you tell me. You're the designers. Rounded corners might be nice, but again, you tell me.

Font styles to use
Serif
Sans Serif

Colors
3276b5
5c5c5c
9d9d9d
fbfbfb

Requirements
Nice to have
• Something different, but still very professional.

```html
<!DOCTYPE html>
<html lang="en">
<head>
<meta charset="utf-8">
<title>Halden Group – Business Cards</title>
<link rel="stylesheet" href="https://fonts.googleapis.com/css2?family=Montserrat:wght@300;400;600&display=swap">
<style>
  :root {
    --backdrop: #e4e7e6;
    --card-dark: #2e3436;
    --card-light: #f7f8f7;
    --brand-blue: #3276b5;
    --tagline-grey: #6b767b;
    --rule-grey: #5c6a70;
    --shadow: rgba(0, 0, 0, 0.18);
  }
  * { margin: 0; padding: 0; box-sizing: border-box; }
  html, body {
    width: 1200px;
    height: 1052px;
    overflow: hidden;
    background: var(--backdrop);
    font-family: "Montserrat", sans-serif;
  }
  .sheet {
    position: relative;
    width: 1200px;
    height: 1052px;
  }
  .card {
    position: absolute;
    left: 190px;
    width: 820px;
    height: 468px;
    border-radius: 4px;
    box-shadow: 0 4px 14px var(--shadow);
    overflow: hidden;
  }
  .card--front { top: 42px; background: var(--card-dark); }
  .card--back  { top: 542px; background: var(--card-light); }

  .vertical {
    position: absolute;
    writing-mode: vertical-rl;
    white-space: nowrap;
  }

  /* Front */
  .brand-name {
    font-weight: 600;
    color: var(--brand-blue);
    letter-spacing: 0.06em;
  }
  .card--front .brand-name {
    left: 380px;
    top: 50%;
    transform: translateY(-50%);
    font-size: 36px;
  }
  .tagline {
    font-weight: 300;
    font-size: 22px;
    color: var(--tagline-grey);
    letter-spacing: 0.02em;
  }
  .tagline--lead { left: 652px; top: 96px; }
  .tagline--success { left: 138px; top: 170px; }
  .tagline-rule {
    position: absolute;
    width: 3px;
    background: var(--rule-grey);
  }
  .tagline-rule--lead { left: 642px; top: 134px; height: 130px; }
  .tagline-rule--success { left: 128px; top: 212px; height: 130px; }

  /* Back */
  .card--back .brand-name {
    left: 668px;
    top: 150px;
    font-size: 24px;
  }
  .brand-mark {
    position: absolute;
    left: 676px;
    top: 120px;
    width: 14px;
    height: 14px;
    background: var(--brand-blue);
  }
  .contact {
    font-size: 17px;
    line-height: 24px;
    color: var(--brand-blue);
    font-weight: 400;
  }
  .contact--phone   { left: 506px; top: 130px; }
  .contact--email   { left: 404px; top: 140px; }
  .contact--address { left: 300px; top: 158px; }
  .contact--web     { left: 196px; top: 170px; }
</style>
</head>
<body>
<main class="sheet">
  <section class="card card--front" aria-label="Card front">
    <span class="vertical tagline tagline--lead">providing leadership</span>
    <span class="tagline-rule tagline-rule--lead"></span>
    <span class="vertical brand-name">HALDEN GROUP</span>
    <span class="vertical tagline tagline--success">delivering success</span>
    <span class="tagline-rule tagline-rule--success"></span>
  </section>

  <section class="card card--back" aria-label="Card back">
    <span class="brand-mark"></span>
    <span class="vertical brand-name">HALDEN GROUP</span>
    <p class="vertical contact contact--phone">1 (888) 555-0173</p>
    <p class="vertical contact contact--email">info@haldengroup.com<br>marketing@haldengroup.com</p>
    <p class="vertical contact contact--address">4150 Crestline Avenue<br>Tampa, FL 33602</p>
    <p class="vertical contact contact--web">www.haldengroup.com</p>
  </section>
</main>
</body>
</html>
```